Top business card designs - show off your work!

Calling all [url removed, login to view] designers! We are giving away $1000 to the best business card design on [url removed, login to view]!

Why enter? 2 reasons:
1) $1000 main prize for the best design
2) The chance to show off your best designs to prospective employers - we will not be sealing the contest.

Here's the rules:
1) Designs should not infringe on the copyright of any existing company or designer
2) Designs should not include real personal details (use fake names and details like Alex Marlow)
3) You may include designs you have done for previous clients

Good luck!!!

```html
<!DOCTYPE html>
<html lang="en">
<head>
<meta charset="utf-8">
<title>Studio Northway – Business Card</title>
<link rel="stylesheet" href="https://fonts.googleapis.com/css2?family=Roboto:wght@400;500&family=Tinos:wght@400;700&display=swap">
<style>
  :root {
    --backdrop: #d8cbb5;
    --card-black: #050505;
    --rose: #c98a90;
    --rose-light: #f2d6d9;
    --rose-deep: #b86c76;
    --olive: #4b4f3f;
    --olive-dark: #3c3f33;
    --cream: #f7f1ec;
    --gold: #e8c24a;
    --gold-soft: #f3e08a;
    --ink-blue: #3a3f9a;
    --ink-rose: #8d3e57;
    --brand-grey: #2c2c2c;
  }
  * { margin: 0; padding: 0; box-sizing: border-box; }
  html, body { width: 1200px; height: 800px; overflow: hidden; }
  body { background: var(--backdrop); position: relative; }

  .card {
    position: absolute;
    width: 520px; height: 300px;
    top: 250px;
    overflow: hidden;
    box-shadow: 0 10px 24px rgba(0,0,0,0.35);
  }
  .card svg { position: absolute; inset: 0; width: 100%; height: 100%; }
  .card--front { left: 50px; background: var(--card-black); }
  .card--back { left: 630px; }

  .brand {
    position: absolute;
    display: flex; align-items: center; gap: 12px;
    font-family: "Roboto", Arial, sans-serif;
    font-weight: 400;
    letter-spacing: 1px;
    white-space: nowrap;
  }
  .brand__mark { display: block; background: var(--gold); }
  .card--front .brand {
    left: 0; right: 0; top: 128px; justify-content: center;
    color: #ffffff; font-size: 26px;
  }
  .card--front .brand__mark { width: 30px; height: 30px; }
  .card--back .brand {
    left: 228px; top: 36px;
    color: var(--brand-grey); font-size: 22px;
  }
  .card--back .brand__mark { width: 24px; height: 24px; }

  .tagline {
    position: absolute; left: 26px; top: 150px; width: 200px;
    font-family: "Tinos", "Times New Roman", serif;
    color: var(--gold); font-size: 17px; line-height: 1.05;
    text-align: center; text-transform: uppercase;
  }
  .services {
    position: absolute; left: 26px; top: 196px; width: 200px;
    list-style: none;
    font-family: "Tinos", "Times New Roman", serif;
    color: var(--gold-soft); font-size: 14px; line-height: 1.1;
    text-align: center;
  }
  .holder-name {
    position: absolute; left: 300px; top: 118px; width: 200px;
    font-family: "Roboto", Arial, sans-serif;
    color: var(--ink-blue); font-size: 24px; text-align: center;
  }
  .profile-note {
    position: absolute; left: 300px; top: 168px; width: 200px;
    font-family: "Roboto", Arial, sans-serif;
    color: var(--ink-rose); font-size: 17px; line-height: 1.15;
    text-align: center;
  }
</style>
</head>
<body>

  <section class="card card--front" aria-label="Card front">
    <svg viewBox="0 0 520 300" preserveAspectRatio="none" aria-hidden="true">
      <path d="M0,120 Q20,230 110,300 L0,300 Z" fill="var(--rose)"/>
      <circle cx="18" cy="285" r="26" fill="var(--rose-light)" opacity="0.55"/>
      <path d="M410,0 Q470,90 520,190 L520,0 Z" fill="var(--rose)"/>
      <circle cx="505" cy="16" r="24" fill="var(--rose-light)" opacity="0.55"/>
    </svg>
    <div class="brand"><span class="brand__mark"></span>STUDIO NORTHWAY</div>
  </section>

  <section class="card card--back" aria-label="Card back">
    <svg viewBox="0 0 520 300" preserveAspectRatio="none" aria-hidden="true">
      <defs>
        <linearGradient id="roseFade" x1="0" y1="0" x2="0.4" y2="1">
          <stop offset="0" stop-color="var(--cream)"/>
          <stop offset="0.45" stop-color="var(--rose-light)"/>
          <stop offset="1" stop-color="var(--rose-deep)"/>
        </linearGradient>
      </defs>
      <rect width="520" height="300" fill="url(#roseFade)"/>
      <path d="M0,0 L520,0 L520,22 Q330,10 200,0 Z" fill="var(--olive-dark)"/>
      <path d="M0,0 L200,0 Q120,20 0,80 Z" fill="var(--olive)"/>
      <path d="M0,80 Q110,30 200,0 Q160,50 250,110 Q210,200 250,300 L0,300 Z" fill="var(--olive)"/>
      <path d="M0,80 Q110,30 200,0 Q150,40 40,95 Z" fill="var(--cream)" opacity="0.9"/>
    </svg>
    <div class="brand"><span class="brand__mark"></span>STUDIO NORTHWAY</div>
    <p class="tagline">We build your<br>online presence</p>
    <ul class="services">
      <li>&gt;&gt;Website Design&lt;&lt;</li>
      <li>&gt;&gt;SEO &amp; Online Marketing&lt;&lt;</li>
      <li>&gt;&gt;Graphics Design&lt;&lt;</li>
    </ul>
    <p class="holder-name">Alex Marlow</p>
    <p class="profile-note">Place Your<br>Social Profile<br>Link here</p>
  </section>

</body>
</html>
```